Business Card Design for BrightlaneReach.com

--I need a business card design for my company BrightlaneReach.com

I have attached my logo...I want the brightlane reach logo on the front of the business card, and then I want The Brightlane Chief on the back of it with my information.

I would like to see a light colored background as well as a dark colored background

FRONT:
BRIGHTLANE REACH LOGO
247 E. Pelham Row
5th Floor
San Diego CA 92384
www.BrightlaneReach.com

Advanced Website & App Development
Websites, Apps, Online Voucher Systems

Leading Edge Marketing Services
SMS, VB, SMM, SEM,

BACK:
BRIGHTLANE CHIEF LOGO
Dorian Welker
The Brightlane Chief
Call Or Text: 555-204-3378
Dorian@BrightlaneChief.com
www.BrightlaneChief.com

Target Market(s)

small business owners

Industry/Entity Type

Business Consultant

Contact Information for Business Card

FRONT:
BRIGHTLANE REACH LOGO
247 E. Pelham Row
5th Floor
San Diego CA 92384
www.BrightlaneReach.com

SMS, VB, SMM, SEM,

BACK:
BRIGHTLANE CHIEF LOGO
Dorian Welker
The Brightlane Chief
Dorian@BrightlaneChief.com
www.BrightlaneChief.com

Requirements
Must have
• add this quote on it somewhere, anywhere,preferrably on back
• "The Fastest Way To Success Is To Take Action”
• — Dorian Welker, Brightlane Chief
Nice to have
• open
Should not have
• red

```html
<!DOCTYPE html>
<html lang="en">
<head>
<meta charset="utf-8">
<title>Brightlane Reach – Business Cards</title>
<link href="https://fonts.googleapis.com/css2?family=Montserrat:wght@400;500;600;700&display=swap" rel="stylesheet">
<style>
  :root {
    --brand-blue: #1a6fa8;
    --ink-black: #050505;
    --paper-white: #ffffff;
    --soft-grey: #9a9a9a;
    --text-dark: #222222;
    --text-grey: #555555;
    --backdrop: #e9e6e1;
  }
  * { box-sizing: border-box; margin: 0; padding: 0; }
  html, body {
    width: 1200px; height: 1200px; overflow: hidden;
    background: var(--backdrop);
    font-family: "Montserrat", sans-serif;
  }
  .canvas {
    position: relative; width: 1200px; height: 1200px;
    display: flex; flex-direction: column; align-items: center; justify-content: center; gap: 48px;
  }
  .card {
    position: relative; width: 860px; height: 491px; overflow: hidden;
    box-shadow: 0 10px 30px rgba(0,0,0,0.18);
  }

  /* Front — dark */
  .card--front { background: var(--ink-black); color: var(--paper-white); }
  .services-tab {
    position: absolute; left: 0; top: 0; width: 390px; height: 80px;
    background: var(--brand-blue); border-bottom-right-radius: 40px;
    padding: 16px 24px; font-weight: 700; font-size: 15px; line-height: 1.45;
  }
  .services-note {
    position: absolute; left: 410px; top: 14px;
    color: var(--soft-grey); font-size: 13px; font-weight: 500; line-height: 1.35;
  }
  .front-logo {
    position: absolute; left: 90px; top: 185px;
    color: var(--brand-blue); font-size: 52px; font-weight: 500; letter-spacing: 6px;
  }
  .address {
    position: absolute; left: 520px; top: 300px;
    display: flex; gap: 16px; font-size: 18px; line-height: 1.5; font-weight: 500;
  }
  .web-line {
    position: absolute; left: 520px; top: 415px;
    display: flex; align-items: center; gap: 16px;
    color: var(--brand-blue); font-size: 18px; font-weight: 500;
  }
  .icon { width: 26px; height: 26px; flex: none; }

  /* Back — light */
  .card--back { background: var(--paper-white); }
  .back-logo {
    position: absolute; right: 60px; top: 60px;
    color: var(--brand-blue); font-size: 48px; font-weight: 500; letter-spacing: 5px;
  }
  .person { position: absolute; left: 150px; top: 215px; }
  .person-name { color: var(--brand-blue); font-size: 26px; font-weight: 700; letter-spacing: 1px; }
  .person-title { color: var(--text-dark); font-size: 22px; font-weight: 500; margin-top: 4px; }
  .divider {
    position: absolute; left: 130px; top: 298px; width: 430px; height: 2px; background: var(--brand-blue);
  }
  .contacts {
    position: absolute; left: 130px; top: 312px; list-style: none;
    font-size: 17px; color: var(--text-grey); font-weight: 500;
  }
  .contacts li { display: flex; align-items: center; gap: 16px; height: 32px; }
  .contacts .label { color: var(--brand-blue); }
  .quote-band {
    position: absolute; right: 0; bottom: 0; width: 540px; height: 62px;
    background: var(--brand-blue); border-top-left-radius: 40px; border-top-right-radius: 40px;
    color: var(--paper-white); font-size: 18px; font-weight: 500;
    display: flex; align-items: center; justify-content: center;
  }
</style>
</head>
<body>
<main class="canvas">

  <section class="card card--front" aria-label="Front of card">
    <div class="services-tab">Leading Edge Marketing Services<br>SMS, VB, SMM, SEM</div>
    <p class="services-note">Advanced Website &amp; App Development<br>Websites, Apps, Online Voucher Systems</p>
    <div class="front-logo">BRIGHTLANE REACH</div>
    <div class="address">
      <svg class="icon" viewBox="0 0 24 24" aria-hidden="true"><path d="M12 3 2 12h3v9h5v-6h4v6h5v-9h3z" fill="#1a6fa8"/></svg>
      <p>247 E. Pelham Row<br>5th Floor<br>San Diego CA 92384</p>
    </div>
    <div class="web-line">
      <svg class="icon" viewBox="0 0 24 24" aria-hidden="true"><circle cx="12" cy="12" r="11" fill="#1a6fa8"/><g fill="none" stroke="#050505" stroke-width="1.3"><circle cx="12" cy="12" r="6.5"/><ellipse cx="12" cy="12" rx="3" ry="6.5"/><path d="M5.5 12h13"/></g></svg>
      <span>www.BrightlaneReach.com</span>
    </div>
  </section>

  <section class="card card--back" aria-label="Back of card">
    <div class="back-logo">BRIGHTLANE CHIEF</div>
    <div class="person">
      <h1 class="person-name">DORIAN WELKER</h1>
      <p class="person-title">The Brightlane Chief</p>
    </div>
    <div class="divider"></div>
    <ul class="contacts">
      <li>
        <svg class="icon" viewBox="0 0 24 24" aria-hidden="true"><path d="M6.6 10.8a15 15 0 0 0 6.6 6.6l2.2-2.2a1 1 0 0 1 1-.25 11.4 11.4 0 0 0 3.6.57 1 1 0 0 1 1 1V20a1 1 0 0 1-1 1A17 17 0 0 1 3 4a1 1 0 0 1 1-1h3.5a1 1 0 0 1 1 1c0 1.25.2 2.45.57 3.57a1 1 0 0 1-.25 1z" fill="#1a6fa8"/></svg>
        <span><span class="label">Call Or Text:</span> 555-204-3378</span>
      </li>
      <li>
        <svg class="icon" viewBox="0 0 24 24" aria-hidden="true"><rect x="2" y="5" width="20" height="14" rx="1" fill="#1a6fa8"/><path d="M2.5 5.5 12 13l9.5-7.5" fill="none" stroke="#fff" stroke-width="1.4"/></svg>
        <span>Dorian@BrightlaneChief.com</span>
      </li>
      <li>
        <svg class="icon" viewBox="0 0 24 24" aria-hidden="true"><circle cx="12" cy="12" r="11" fill="#1a6fa8"/><g fill="none" stroke="#fff" stroke-width="1.3"><circle cx="12" cy="12" r="6.5"/><ellipse cx="12" cy="12" rx="3" ry="6.5"/><path d="M5.5 12h13"/></g></svg>
        <span>www.BrightlaneChief.com</span>
      </li>
    </ul>
    <blockquote class="quote-band">“The Fastest Way To Success Is To Take Action”</blockquote>
  </section>

</main>
</body>
</html>
```